Brightmark Power website design

Electrical contractor in Perth that services the domestic and commercial markets. our services include but not limited to:

New Home Installations and Design
Commercial Shop Fit Outs
Rewires
Renovations
Switchboard Upgrades
Kitchen and Bathroom Renovations
RCD'S (Safety Switches)
Smoke Alarms
Power points
Security Lighting
Energy Efficient LED Lighting Designs
Garden Lighting
Downlights
General Electrical Maintenance
TV and Phone Points
Home Theatre Installs
Safety Certificates
24hr Call out service
Electric Hot Water Units
Credit cards accepted

www.sociabook.example/brightmarkpower

Contractor

5+ page

Sans Serif

acd037
fbee3e

• contact page, services page, about us, careers page, somewhere I can put some testimonials, somewhere potential clients can book our services online, on the homepage somewhere showing that we can provide 24/7 emergency service
• icon stating that we accept all major credit cards

```html
<!DOCTYPE html>
<html lang="en">
<head>
<meta charset="utf-8">
<title>Brightmark Power</title>
<link rel="stylesheet" href="https://fonts.googleapis.com/css2?family=Open+Sans:ital,wght@0,400;0,600;0,700;1,400&family=Oswald:wght@300&display=swap">
<style>
:root{
  --lime:#acd037;
  --yellow:#fbee3e;
  --navy:#0f4a7e;
  --grey:#8a8a8a;
  --text:#555;
  --footer:#f6f7ea;
  --line:#d9d9d9;
}
*{box-sizing:border-box;margin:0;padding:0}
html,body{width:865px;height:1200px;overflow:hidden;background:#fff}
body{position:relative;font-family:"Open Sans",Arial,sans-serif;color:var(--text)}
.abs{position:absolute}

/* header */
.brand-dot{left:108px;top:26px;width:64px;height:64px;border-radius:50%;background:var(--lime)}
.brand-name{left:205px;top:26px;font-size:31px;line-height:34px;font-weight:600;color:var(--lime);white-space:nowrap}
.licence{left:314px;top:100px;font-size:8px;font-weight:600;color:var(--navy)}
.contact-top{top:51px;display:flex;align-items:center;gap:5px;font-size:12.5px;font-style:italic;color:var(--navy);white-space:nowrap}
.contact-top .ico{width:20px;height:20px;border-radius:50%;background:var(--lime);display:flex;align-items:center;justify-content:center}
.contact-sep{left:646px;top:44px;width:1px;height:34px;background:var(--yellow)}

/* nav */
.nav{left:93px;top:126px;width:679px;height:48px;border-top:1px solid var(--lime);border-bottom:3px double var(--lime)}
.nav a{position:absolute;top:0;height:100%;display:flex;align-items:center;white-space:nowrap;font-size:12px;font-weight:600;color:var(--navy);text-decoration:none}
.nav a.active{left:0;width:68px;justify-content:center;background:var(--lime);color:#fff}

/* hero */
.hero{left:0;top:190px;width:865px;height:302px;background:linear-gradient(90deg,#b99a5e 0%,#7d6a55 30%,#5a4d45 60%,#3d3a3a 100%)}
.hero-title{right:19px;top:238px;font-family:"Oswald",sans-serif;font-weight:300;font-size:60px;color:#fff;letter-spacing:-1px;line-height:1;white-space:nowrap}
.hero-copy{right:24px;top:318px;width:380px;text-align:right;font-size:11.5px;line-height:17px;color:#fff}
.hero-btn{left:725px;top:413px;width:118px;height:33px;border:1px solid var(--yellow);color:var(--yellow);font-size:9.5px;display:flex;align-items:center;justify-content:center}

/* welcome */
.section-title{left:0;width:865px;text-align:center;font-size:17px;font-weight:400;color:var(--grey);white-space:nowrap}
.section-title .lime{color:var(--lime);font-weight:600}
.section-title .navy{color:var(--navy);font-weight:700}
.rule{height:3px;border-top:1px solid var(--line);border-bottom:1px solid var(--line)}
.welcome-copy{left:114px;top:570px;width:638px;text-align:center;font-size:11.2px;line-height:17px;color:var(--grey)}

/* services */
.services{left:93px;top:650px;width:679px;height:282px;border-top:1px solid #e4e4e4;background:linear-gradient(180deg,#fff 0%,#fdf9c6 45%,var(--yellow) 100%)}
.card{top:722px;width:197px;height:185px}
.card-featured{background:var(--lime);color:#fff;text-align:center}
.card-featured h3{margin-top:34px;font-size:13px;font-weight:700}
.card-featured p{margin:12px auto 0;width:136px;font-size:10px;line-height:15px}
.card-featured .go{margin:20px auto 0;width:30px;height:30px;border-radius:50%;background:var(--yellow);display:flex;align-items:center;justify-content:center}
.card-photo{display:flex;align-items:flex-end}
.card-photo span{width:100%;padding:24px 10px 8px;font-size:12.5px;font-weight:600;color:var(--yellow);background:linear-gradient(180deg,rgba(0,0,0,0),rgba(15,40,70,.75));white-space:nowrap}
.arrow{top:786px}

/* footer */
.footer{left:0;top:974px;width:865px;height:187px;background:var(--footer)}
.f-col{top:991px}
.f-col h4{font-size:11.5px;font-weight:700;color:var(--navy)}
.f-col .rule{width:60px;margin:6px 0 14px}
.f-links a{display:block;font-size:9px;color:var(--text);text-decoration:none;line-height:17px}
.f-links a.current{color:var(--lime)}
.f-about p{font-size:8.5px;line-height:13px;width:160px}
.subscribe{margin-top:10px;display:flex;width:154px;height:22px}
.subscribe .field{flex:1;background:#e6e8d2;font-size:8.5px;padding:5px 9px;color:#444}
.subscribe .send{width:25px;background:var(--lime);display:flex;align-items:center;justify-content:center}
.badge{margin-top:16px;width:118px;height:32px;border-radius:3px;background:var(--navy)}
.social a{display:flex;align-items:center;gap:12px;font-size:9px;color:var(--text);text-decoration:none;height:29.5px}
.social .c{width:22px;height:22px;border-radius:50%;background:#d6d8c4}
.social .c.on{background:var(--navy)}
.touch li{list-style:none;display:flex;gap:15px;align-items:flex-start;font-size:8.5px;line-height:14px}
.touch svg{flex:none;margin-top:1px}
.bottom{left:0;top:1161px;width:865px;height:39px;background:var(--lime)}
.cards{left:93px;top:1171px;display:flex;gap:5px}
.cards span{width:26px;height:17px;border-radius:2px;background:#f2f2f2;border:1px solid #c9c9c9}
.copyright{right:93px;top:1174px;font-size:8.5px;color:#fff}
</style>
</head>
<body>

<header>
  <div class="abs brand-dot"></div>
  <div class="abs brand-name">Brightmark<br>Power</div>
  <div class="abs licence">EC 20417</div>

  <div class="abs contact-top" style="left:536px">
    <span class="ico"><svg width="11" height="11" viewBox="0 0 12 12"><path d="M6 1a5 5 0 0 0-5 5v3h3V6H2.3a3.7 3.7 0 0 1 7.4 0H8v3h3V6a5 5 0 0 0-5-5z" fill="#fff"/></svg></span>24/7 Support
  </div>
  <div class="abs contact-sep"></div>
  <div class="abs contact-top" style="left:658px">
    <span class="ico"><svg width="11" height="11" viewBox="0 0 12 12"><path d="M3 1l2 2.5-1 1.3a7 7 0 0 0 3.2 3.2l1.3-1L11 9l-1.2 2C5.5 10.8 1.2 6.5 1 2.2z" fill="#fff"/></svg></span>+61 400 555 010
  </div>

  <nav class="abs nav">
    <a class="active" href="#">HOME</a>
    <a href="#" style="left:82px">WHY CHOOSE US</a>
    <a href="#" style="left:210px">SERVICES</a>
    <a href="#" style="left:293px">ABUOT US</a>
    <a href="#" style="left:382px">BLOG</a>
    <a href="#" style="left:444px">CARRER</a>
    <a href="#" style="left:518px">STORE</a>
    <a href="#" style="left:585px">CONTACT US</a>
  </nav>
</header>

<section>
  <div class="abs hero" role="img" aria-label="Photo of a smiling electrician in a yellow hard hat and safety vest testing a switchboard"></div>
  <h1 class="abs hero-title" style="font-weight:300">LIGHTEN UP YOUR LIFE !</h1>
  <p class="abs hero-copy">Lorem ipsum dolor sit amet, consectetur adipiscing elitenean congu mauris in luctus laoreet Ut sed commodo arcu...</p>
  <div class="abs hero-btn">READ MORE</div>
</section>

<section>
  <h2 class="abs section-title" style="top:520px">WELCOME TO <span class="lime">BRIGHTMARK</span> <span class="navy">POWER</span></h2>
  <div class="abs rule" style="left:359px;top:551px;width:147px"></div>
  <p class="abs welcome-copy">Lorem ipsum dolor sit amet, consectetur adipiscing elit. Etiam sodales porta ligula id consequat. Ut lorem est, faucibus ac dui at, pellentesque vehicula dolor. Aliquam maximus diam luctus lectus tristique aliquet. Mauris sed venenatis tellus. In porttitor, odio sed commodo posuere, turpis massa interdum tellus, in euismod lectus ex et lectus.</p>
</section>

<section>
  <div class="abs services"></div>
  <h2 class="abs section-title" style="top:668px"><span class="lime" style="font-weight:400">OUR</span> <span class="navy">SERVICES</span></h2>
  <div class="abs rule" style="left:393px;top:699px;width:80px"></div>

  <svg class="abs arrow" style="left:84px" width="22" height="30" viewBox="0 0 22 30"><path d="M20 2L4 15l16 13-6-13z" fill="#b5b5b5"/></svg>
  <svg class="abs arrow" style="left:758px" width="22" height="30" viewBox="0 0 22 30"><path d="M2 2l16 13L2 28l6-13z" fill="#acd037"/></svg>

  <div class="abs card card-featured" style="left:116px">
    <h3>DOWNLIGHTS</h3>
    <p>Lorem ipsum dolor sit amet, consectetur adipiscing sodales porta etv...</p>
    <div class="go"><svg width="10" height="12" viewBox="0 0 10 12"><path d="M2 1l6 5-6 5" stroke="#acd037" stroke-width="2" fill="none"/></svg></div>
  </div>
  <div class="abs card card-photo" style="left:334px;background:linear-gradient(135deg,#f4f4f4,#cfd3d6)" role="img" aria-label="Photo of a double power point on a white tiled wall">
    <span>SWITCHBOARD UPGRADES</span>
  </div>
  <div class="abs card card-photo" style="left:553px;background:linear-gradient(135deg,#2c3e58,#6b6a66 55%,#b9a98f)" role="img" aria-label="Photo of a dining room with pendant lights and a feature wall">
    <span>ELECTRICAL MAINTENANCE</span>
  </div>
</section>

<footer>
  <div class="abs footer"></div>

  <div class="abs f-col f-links" style="left:93px">
    <h4>Information</h4><div class="rule"></div>
    <a class="current" href="#">Home</a><a href="#">Why choose us</a><a href="#">Services</a><a href="#">About us</a><a href="#">Carrer</a><a href="#">Blog</a><a href="#">Store</a>
  </div>

  <div class="abs f-col f-about" style="left:236px">
    <h4>About us</h4><div class="rule"></div>
    <p>Lorem ipsum dolor sit amet, consr sit adipi scing elit.</p>
    <div class="subscribe"><div class="field">your@email.com</div><div class="send"><svg width="8" height="10" viewBox="0 0 8 10"><path d="M1 0l7 5-7 5z" fill="#fff"/></svg></div></div>
    <div class="badge" role="img" aria-label="Trade association member badge"></div>
  </div>

  <div class="abs f-col social" style="left:472px">
    <h4>Social Media</h4><div class="rule"></div>
    <a href="#"><span class="c on"></span>Sociabook</a>
    <a href="#"><span class="c"></span>Chirper</a>
    <a href="#"><span class="c"></span>Circlespace</a>
    <a href="#"><span class="c"></span>ViewTube</a>
  </div>

  <div class="abs f-col touch" style="left:621px">
    <h4>Get In Touch</h4><div class="rule"></div>
    <ul>
      <li style="height:38px"><svg width="18" height="16" viewBox="0 0 18 16"><path d="M9 1L1 8h2.5v7h4v-4h3v4h4V8H17z" fill="#acd037"/></svg><span>42 Sample Street, Unit 3<br>PO Box 88, Perth WA.</span></li>
      <li style="height:29px"><svg width="18" height="14" viewBox="0 0 12 12"><path d="M3 1l2 2.5-1 1.3a7 7 0 0 0 3.2 3.2l1.3-1L11 9l-1.2 2C5.5 10.8 1.2 6.5 1 2.2z" fill="#acd037"/></svg><span>+ 61 400 555 010</span></li>
      <li style="height:31px"><svg width="18" height="14" viewBox="0 0 18 14"><rect x="5" y="0" width="8" height="3" fill="#acd037"/><rect x="1" y="4" width="16" height="6" rx="1" fill="#acd037"/><rect x="5" y="9" width="8" height="5" fill="#acd037" stroke="#f6f7ea" stroke-width="1"/></svg><span>+ 61 400 555 011</span></li>
      <li><svg width="18" height="13" viewBox="0 0 18 13"><rect x="1" y="1" width="16" height="11" fill="#acd037"/><path d="M1 1l8 6 8-6" stroke="#fff" fill="none"/></svg><span>hello@brightmarkpower.example</span></li>
    </ul>
  </div>

  <div class="abs bottom"></div>
  <div class="abs cards" role="img" aria-label="Accepted payment cards">
    <span></span><span></span><span></span><span></span><span></span><span></span>
  </div>
  <div class="abs copyright">Copyright © 2014 Brightmark Power All rights reserved.</div>
</footer>

</body>
</html>
```